Wordpress Design Project - IT Consulting Services Web Site

Our are starting a new technology services company. We will provide services in software implementation and business intelligence.

We need a beautiful Wordpress web site design. We need a design for the homepage, and one interior content page.

The site must have a very professional and polished look and feel. What I have suggested below are things that I think work, but I am not a designer and I am open to your professional opinions. Please be willing to use your best judgment.

The homepage should have the following elements:
- A Header Area that includes:
o The company logo, and
o navigation (consistent with the interior page)
o a social media link section that includes rss feeds, youtube, facebook, linkedin and tweets
- A Body that includes:
o A slider
o An area that features up to six of the most recent or important posts including a thumbnail and small picture, a title, and a short excerpt for each.
o An area for around 100 words of text and an image
- A footer that includes:
o The company logo
o Contact information

The interior page is relatively simple. It should include the same navigation element as the homepage, and accommodate a one column text layout.

The current site …
You can visit the current site at www.korvelpath.com I built the current site using the “Velthor Quick Pane” premium theme. If you visit this site you get a sense of some of the things I am talking about, but there are things that I do not like about the current site. Here’s what I like and what I don’t like.

What I like about the current site:
- It is reactive – it adapts to the size of the viewing browser
- It has a “metro” feel to it. The company will have an association with Microsoft and having a “metro” theme is a plus, but not a requirement.
- It is different without being hard to navigate – the site the slider is from the “glide cascade widget”, the posts are represented with tiles and rearrange themselves when a topic is selected.

What I don’t like:
- The site lacks a cohesive feel – it feels to me like a bunch of different elements without a single theme that pulls everything together.
- It is not aesthetically appealing to me.
- The tiles in the post section are too big.
- I don’t like the white background – I would prefer a background color and ideally a background that somehow incorporates the graphic in the logo.

About themes
As I said, I used a Velthor theme in my design. I will be happy to continue using this theme, or would be willing to buy a new premium theme, so long as the cost is less than $100 U.S.

Site Map:
What we do
ERP Implementation
Business Intelligence
Who we are
What’s different about us
Principles
Mission, Vision, Values
Actions
How we work
What’s Different About Us
Blogs
What Papers
Presentations
Join
What we are looking for
What are you looking for?
Benefits
Context
Updates

Regarding Pictures
Please do not feel you need to use any of the pictures currently on the site.  Use whatever pictures you feel look best.  Comps are okay. 

It is not necessary to use any of the content on the current site - you do not need to use either the pictures or the text.  Please feel free to use pictures of your choice (comps okay), and/or lorem text.

The top level navigation is the navigation I would like.

Hello all,

Since this is a Wordpress project, it goes without saying I will need to implement this design in Wordpress.  It is not absolutely necessary that a design that matches an existing template (free or not), but a design that does will have an advantage over a design which requires that a new template be coded from scratch.

Thank you.

Target Market(s)

Business executives and potential employees

Industry/Entity Type

Software

Requirements
Nice to have
• It would be nice if the site was reactive.

```html
<!DOCTYPE html>
<html lang="en">
<head>
<meta charset="utf-8">
<title>Korvel Path — ERP Implementations</title>
<link rel="stylesheet" href="https://fonts.googleapis.com/css2?family=Open+Sans:wght@400;600&display=swap">
<style>
  :root {
    --header-bg: #174a6b;
    --hero-deep: #0687cf;
    --hero-light: #25b4ea;
    --accent: #1b93d3;
    --nav-text: #ffffff;
    --page-bg: #eeeceb;
    --text: #666666;
    --heading: #555555;
    --rule: #c9c7c6;
    --footer-bg: #333333;
    --footer-text: #ffffff;
    --font: "Open Sans", Arial, sans-serif;
  }
  * { box-sizing: border-box; margin: 0; padding: 0; }
  html, body { width: 1160px; height: 1200px; overflow: hidden; }
  body { font-family: var(--font); background: var(--page-bg); color: var(--text); position: relative; }

  .site-header { position: absolute; left: 0; top: 0; width: 1160px; height: 130px; background: var(--header-bg); }
  .brand { position: absolute; left: 116px; top: 70px; display: flex; align-items: center; gap: 10px; }
  .brand-name { font-size: 29px; font-weight: 400; color: #ffffff; letter-spacing: -0.5px; }
  .brand-dot { width: 14px; height: 14px; border-radius: 50%; background: var(--accent); }
  .main-nav { position: absolute; right: 116px; top: 48px; display: flex; gap: 35px; }
  .main-nav a { color: var(--nav-text); text-decoration: none; font-size: 14px; font-weight: 600; }
  .main-nav a.is-active { color: #2aa7e0; }
  .social-links { position: absolute; right: 116px; top: 92px; display: flex; gap: 7px; }
  .social-links span { width: 26px; height: 26px; border-radius: 50%; display: block; }
  .social-a { background: #3b5a99; } .social-b { background: #2aa7e0; } .social-c { background: #1a7cb5; }
  .social-d { background: #e32a22; } .social-e { background: #f4901e; }

  .hero { position: absolute; left: 0; top: 130px; width: 1160px; height: 473px;
    background: radial-gradient(ellipse at 30% 45%, var(--hero-light) 0%, #0c9ad9 45%, var(--hero-deep) 100%); }
  .hero-art { position: absolute; left: 130px; top: 20px; width: 400px; height: 430px;
    background: linear-gradient(160deg, rgba(255,255,255,0.28) 0%, rgba(150,215,245,0.22) 50%, rgba(12,154,217,0.05) 100%); }
  .hero-copy { position: absolute; left: 582px; top: 80px; color: #ffffff; width: 470px; }
  .hero-title { font-weight: 400; font-size: 68px; line-height: 76px; }
  .hero-subtitle { font-weight: 400; font-size: 46px; line-height: 56px; margin-top: 2px; }
  .hero-text { font-size: 15.5px; line-height: 21.5px; text-transform: uppercase; margin-top: 14px; letter-spacing: 0.2px; }
  .btn-more { display: inline-block; margin-top: 20px; margin-left: 4px; width: 136px; height: 39px; border-radius: 20px;
    background: linear-gradient(#ffffff, #dcdcdc); color: #9a9a9a; font-size: 15px; line-height: 39px; text-align: center; text-decoration: none; }
  .slider-dots { position: absolute; left: 555px; top: 446px; display: flex; gap: 6px; }
  .slider-dots span { width: 13px; height: 13px; border-radius: 50%; background: #8f9aa3; border: 1px solid #6a7680; }
  .slider-dots span.is-current { background: #3a444c; }

  .recent-posts { position: absolute; left: 116px; top: 617px; width: 928px; }
  .section-title { font-size: 14px; font-weight: 400; color: var(--heading); height: 21px; }
  .section-bar { height: 5px; background: var(--accent); margin-top: 4px; }
  .post-grid { display: grid; grid-template-columns: 319px 319px 290px; row-gap: 28px; margin-top: 19px; }
  .post { display: flex; gap: 8px; }
  .post-thumb { width: 59px; height: 59px; border: 2px solid #ffffff; flex: none; box-shadow: 0 0 1px #aaa;
    background: linear-gradient(135deg, #d9dde0, #7c8590); }
  .post-title { font-size: 12.5px; color: var(--accent); font-weight: 400; line-height: 16px; }
  .post-excerpt { font-size: 11px; line-height: 15px; width: 232px; }

  .divider { position: absolute; left: 116px; top: 841px; width: 928px; height: 1px; background: var(--rule); }

  .about-block { position: absolute; left: 116px; top: 864px; width: 928px; display: flex; gap: 10px; }
  .about-photo { width: 290px; height: 173px; flex: none; background: linear-gradient(120deg, #f4f4f4 0%, #c9cdd2 45%, #4d5661 100%); }
  .about-kicker { font-size: 11px; color: var(--heading); margin-top: -2px; }
  .about-heading { font-size: 11.5px; color: var(--accent); font-weight: 400; margin-top: 6px; }
  .about-text { font-size: 11px; line-height: 17.5px; margin-top: 1px; }
  .about-group + .about-group { margin-top: 16px; }

  .site-footer { position: absolute; left: 0; top: 1062px; width: 1160px; height: 138px; background: var(--footer-bg); color: var(--footer-text); }
  .footer-brand { position: absolute; left: 116px; top: 62px; display: flex; align-items: center; gap: 10px; }
  .footer-brand .brand-name { font-size: 27px; }
  .copyright { position: absolute; left: 116px; top: 111px; font-size: 11px; }
  .footer-col { position: absolute; top: 10px; font-size: 11.5px; line-height: 17px; }
  .footer-col h3 { font-size: 14px; font-weight: 400; color: var(--accent); margin-bottom: 17px; }
  .footer-about { left: 436px; width: 292px; text-align: justify; }
  .footer-contact { left: 766px; width: 280px; }
  .footer-contact h3 { margin-bottom: 5px; }
  .footer-contact p + p { margin-top: 9px; }
  .footer-contact .email { color: var(--accent); }
</style>
</head>
<body>
  <header class="site-header">
    <div class="brand"><span class="brand-name">Korvel Path</span><span class="brand-dot"></span></div>
    <nav class="main-nav">
      <a class="is-active" href="#">WHAT WE DO</a>
      <a href="#">WHO WE ARE</a>
      <a href="#">HOW WE WORK</a>
      <a href="#">JOIN US</a>
      <a href="#">CONTACT US</a>
    </nav>
    <div class="social-links">
      <span class="social-a" aria-label="Social network link"></span>
      <span class="social-b" aria-label="Social network link"></span>
      <span class="social-c" aria-label="Social network link"></span>
      <span class="social-d" aria-label="Video channel link"></span>
      <span class="social-e" aria-label="News feed link"></span>
    </div>
  </header>

  <section class="hero">
    <div class="hero-art" role="img" aria-label="Slide illustration about business systems"></div>
    <div class="hero-copy">
      <h1 class="hero-title">ERP</h1>
      <h2 class="hero-subtitle">IMPLEMENTATIONS</h2>
      <p class="hero-text">Every services firm is made up of people, processes and tools. At Korvel Path, we put people first, tailoring everything we do to find, hire, train, and keep the very best people. Because once you have the best people everything else follows.</p>
      <a class="btn-more" href="#">LEARN MORE</a>
    </div>
    <div class="slider-dots"><span></span><span></span><span class="is-current"></span></div>
  </section>

  <section class="recent-posts">
    <h2 class="section-title">MOST RECENT POSTS</h2>
    <div class="section-bar"></div>
    <div class="post-grid">
      <article class="post"><div class="post-thumb" role="img" aria-label="Photo of colleagues meeting"></div><div><h3 class="post-title">growth is essential</h3><p class="post-excerpt">Growth in a company typically means some good things are happening, but at Korvel Path we believe growth is essential..</p></div></article>
      <article class="post"><div class="post-thumb" role="img" aria-label="Photo of a business team standing"></div><div><h3 class="post-title">amet, consectetur adipisicing</h3><p class="post-excerpt">Growth in a company typically means some good things are happening, but at Korvel Path we believe growth is essential..</p></div></article>
      <article class="post"><div class="post-thumb" role="img" aria-label="Photo of a boardroom meeting"></div><div><h3 class="post-title">accusantium doloremq</h3><p class="post-excerpt">Growth in a company typically means some good things are happening, but at Korvel Path we believe growth is essential..</p></div></article>
      <article class="post"><div class="post-thumb" role="img" aria-label="Photo of people holding question marks"></div><div><h3 class="post-title">laudantium, totam rem aperiam</h3><p class="post-excerpt">Growth in a company typically means some good things are happening, but at Korvel Path we believe growth is essential..</p></div></article>
      <article class="post"><div class="post-thumb" role="img" aria-label="Portrait photo of a businessman"></div><div><h3 class="post-title">ignissimos ducimus qui</h3><p class="post-excerpt">Growth in a company typically means some good things are happening, but at Korvel Path we believe growth is essential..</p></div></article>
      <article class="post"><div class="post-thumb" role="img" aria-label="Photo of hands over a meeting table"></div><div><h3 class="post-title">occaecati cupiditate non provident</h3><p class="post-excerpt">Growth in a company typically means some good things are happening, but at Korvel Path we believe growth is essential..</p></div></article>
    </div>
  </section>

  <div class="divider"></div>

  <section class="about-block">
    <div class="about-photo" role="img" aria-label="Photo of a smiling business team"></div>
    <div>
      <div class="about-group">
        <p class="about-kicker">People, Processes and Tools</p>
        <h3 class="about-heading">Putting People First</h3>
        <p class="about-text">Every services firm is made up of people, processes and tools. At Korvel Path, we put people first, tailoring everything we do to find, hire, train, and keep the very best people. Because once you have the best people everything else follows.</p>
      </div>
      <div class="about-group">
        <p class="about-kicker">Korvel Path</p>
        <h3 class="about-heading">What's the idea?</h3>
        <p class="about-text">The idea is an old one but a great one.&nbsp; Harlan Wescott Brill was an American writer credited with creating the phrase "The American Dream".&nbsp; It's the idea that your success should depend on your ability and achievements, not on where you started out.&nbsp; It's an idea we try to live up to.</p>
      </div>
    </div>
  </section>

  <footer class="site-footer">
    <div class="footer-brand"><span class="brand-name">Korvel Path</span><span class="brand-dot"></span></div>
    <p class="copyright">© 2013 korvelpath&nbsp; | All Rights Reserved.</p>
    <div class="footer-col footer-about">
      <h3>About Korvel Path</h3>
      <p>Korvel Path provides technology services in a variety of areas. What makes us different is our focus on finding, training and retaining the very best people, who focus on providing our customers with the very best service.</p>
    </div>
    <div class="footer-col footer-contact">
      <h3>Contact info</h3>
      <p>Address:<br>Street 4417, Lower Fenwick 5820, Region</p>
      <p>Telephone: 2046 3318<br>Fax: 7731 0592<br><span class="email">Email: hello@korvelpath.com</span></p>
    </div>
  </footer>
</body>
</html>
```